Startup needs a Powerpoint presentation for investors

We are raising capital and we need to show the project to new investors. Our website is: plumvane.es.

We need the presentation to be modified by us with new numbers, text, etc.

We need to redesign everything: chats, font (we like Lato, but we are open to suggestions), etc.

We are open to new ideas, but we have preference for Lato font and our color palette. We like clean presentations (white backgrounds) and we use color or emojis to highlight things.

You can see how we design entering our app: app.plumvane.es
Updates

To win the contest you do not need to design every slide. You can choose to design some of them for us to see how it would be and after you win you can design the others.

Industry/Entity Type

Startup

Font styles to use
Other font styles liked:
• Lato

Requirements
Must have
• Editable for us.
Nice to have
• Use our color palette (you can use more colors if you like):
• Black: #575756
• Grey 1: #B9B9B9
• Grey 2: #575756 (A = 15)
• Grey 3: #F9F9F9
• White: #FFFFFF
• Green 1: #197A45
• Green 2: #197A45 (A = 11)

```html
<!DOCTYPE html>
<html lang="en">
<head>
<meta charset="utf-8">
<title>Plumvane – Investor Deck</title>
<link rel="stylesheet" href="https://fonts.googleapis.com/css2?family=Open+Sans:wght@400;600;700&display=swap">
<style>
  :root{
    --stage:#111111;
    --slide:#f9f9f9;
    --white:#ffffff;
    --ink:#575756;
    --band:#7f7f7f;
    --band-light:#e6e6e6;
    --tri-dark:#333333;
    --tri-light:#b9b9b9;
    --green:#197a45;
    --card:#ffffff;
  }
  *{margin:0;padding:0;box-sizing:border-box}
  html,body{width:800px;height:1200px;overflow:hidden;background:var(--stage)}
  body{font-family:"Open Sans",Arial,sans-serif;position:relative}
  .slide{position:absolute;left:100px;width:600px;height:338px;background:var(--slide);overflow:hidden}
  .slide--cover{top:53px}
  .slide--problem{top:431px}
  .slide--origin{top:809px}
  .deco{position:absolute;inset:0}

  .brand{position:absolute;display:flex;align-items:center;color:var(--green);font-weight:600}
  .brand__dot{background:var(--green);border-radius:50%;flex:none}
  .brand--hero{left:0;right:0;top:82px;justify-content:center;font-size:54px;gap:22px;letter-spacing:-0.5px}
  .brand--hero .brand__dot{width:40px;height:40px}
  .brand--footer{right:44px;bottom:18px;font-size:20px;gap:10px}
  .brand--footer .brand__dot{width:18px;height:18px}
  .brand--corner{right:28px;top:16px;font-size:12px;gap:6px}
  .brand--corner .brand__dot{width:12px;height:12px}

  .tagline{position:absolute;left:224px;top:276px;color:var(--white);font-weight:600;font-size:20px}
  .section-title{position:absolute;left:38px;top:141px;color:var(--white);font-weight:700;font-size:19px;letter-spacing:.3px}
  .section-sub{position:absolute;left:38px;top:172px;color:var(--white);font-size:14px}
  .origin-title{position:absolute;left:86px;top:26px;color:var(--ink);font-weight:700;font-size:14px}
  .origin-sub{position:absolute;left:86px;top:52px;color:var(--ink);font-size:14px}

  .step{position:absolute;top:122px;width:236px;height:188px;background:var(--card);border-radius:8px}
  .step--gather{left:32px}
  .step--buy{left:332px}
  .step__num{position:absolute;left:12px;top:12px;width:24px;height:24px;border:2px solid var(--green);border-radius:50%;color:var(--green);font-weight:700;font-size:13px;display:flex;align-items:center;justify-content:center}
  .step__art{position:absolute;left:36px;top:34px;width:164px;height:108px;border-radius:4px}
  .step--gather .step__art{background:linear-gradient(90deg,#c9df6a 0%,#f4f4f0 45%,#3f8aa6 100%);opacity:.85}
  .step--buy .step__art{background:linear-gradient(135deg,#f1d9cf,#e9e5e0 60%,#c7c3bf)}
  .step__caption{position:absolute;left:0;right:0;bottom:30px;text-align:center;color:var(--green);font-size:14px}
</style>
</head>
<body>

<section class="slide slide--cover">
  <div class="brand brand--hero"><span class="brand__dot"></span>Plumvane</div>
  <svg class="deco" viewBox="0 0 600 338" aria-hidden="true">
    <rect x="0" y="243" width="600" height="95" fill="var(--band)"/>
    <polygon points="504,243 600,243 552,290" fill="var(--tri-dark)"/>
    <polygon points="600,243 600,338 504,338" fill="var(--tri-light)"/>
    <line x1="0" y1="290" x2="212" y2="290" stroke="var(--white)" stroke-width="2"/>
    <circle cx="213" cy="290" r="3" fill="var(--white)"/>
  </svg>
  <p class="tagline">Play Lottery With Your Friends</p>
</section>

<section class="slide slide--problem">
  <svg class="deco" viewBox="0 0 600 338" aria-hidden="true">
    <polygon points="600,0 600,122 500,122" fill="var(--white)"/>
    <polygon points="405,216 600,216 600,338 300,338" fill="var(--white)"/>
    <rect x="0" y="122" width="600" height="94" fill="var(--band)"/>
    <polygon points="504,122 600,122 552,168" fill="var(--tri-dark)"/>
    <polygon points="600,122 600,216 504,216" fill="var(--tri-light)"/>
    <line x1="0" y1="168" x2="534" y2="168" stroke="var(--white)" stroke-width="2"/>
    <circle cx="535" cy="168" r="3" fill="var(--white)"/>
  </svg>
  <h2 class="section-title">PROBLEM</h2>
  <p class="section-sub">Playing lottery in group is a nightmare</p>
  <div class="brand brand--footer"><span class="brand__dot"></span>Plumvane</div>
</section>

<section class="slide slide--origin">
  <svg class="deco" viewBox="0 0 600 338" aria-hidden="true">
    <rect x="0" y="0" width="600" height="95" fill="var(--band-light)"/>
    <polygon points="0,0 0,95 96,95" fill="var(--tri-light)"/>
    <polygon points="4,0 94,0 52,44" fill="var(--tri-dark)"/>
    <line x1="64" y1="47" x2="600" y2="47" stroke="var(--white)" stroke-width="2"/>
    <circle cx="65" cy="47" r="3" fill="var(--white)"/>
  </svg>
  <h2 class="origin-title">Plumvane was created to solve a pain we had:</h2>
  <p class="origin-sub">Play lottery with our friends</p>
  <div class="brand brand--corner"><span class="brand__dot"></span>Plumvane</div>

  <article class="step step--gather">
    <span class="step__num">1</span>
    <div class="step__art" role="img" aria-label="Cartoon of a running banknote being chased"></div>
    <p class="step__caption">Gather everyone's money</p>
  </article>
  <article class="step step--buy">
    <span class="step__num">2</span>
    <div class="step__art" role="img" aria-label="Close-up photo of a printed lottery ticket"></div>
    <p class="step__caption">Purchase the lottery ticket</p>
  </article>
</section>

</body>
</html>
```